Solar appointment reminder card

We are looking for a new design for our appointment reminder card since we have changed our logo. The card should have the new logo along with space for the employee to hand write the customers appointment date, time, the employees name and phone number.
I've uploaded what our old basic appointment card looked like and our new logo.

The cards should be in a standard business card size and could be horizontal or vertical.

```html
<!DOCTYPE html>
<html lang="en">
<head>
<meta charset="utf-8">
<title>Brightfield Solar – Appointment Card</title>
<link rel="stylesheet" href="https://fonts.googleapis.com/css2?family=Open+Sans:wght@400;600;800&display=swap">
<style>
  :root {
    --bg: #e6e4e1;
    --charcoal: #2b2b2b;
    --charcoal-light: #4a4a4a;
    --sun-yellow: #fcbf1e;
    --sun-orange: #f7931e;
    --paper: #ffffff;
    --ink: #333333;
    --rule: #c9c9c9;
  }
  * { margin: 0; padding: 0; box-sizing: border-box; }
  html, body {
    width: 1200px; height: 800px; overflow: hidden;
    background: var(--bg);
    font-family: "Open Sans", Arial, sans-serif;
  }
  .sheet {
    width: 1200px; height: 800px;
    display: flex; align-items: center; justify-content: center; gap: 40px;
  }
  .card {
    width: 540px; height: 309px;
    box-shadow: 0 6px 18px rgba(0,0,0,.18);
    background: var(--paper);
  }
  .card svg { display: block; width: 540px; height: 309px; }
  .brand-name { font-family: "Open Sans", Arial, sans-serif; font-weight: 800; fill: var(--sun-orange); }
  .brand-dot { fill: var(--sun-yellow); }
  .web-address { font-family: "Open Sans", Arial, sans-serif; font-weight: 400; fill: var(--ink); font-size: 16px; }
  .appointment-title { font-family: "Open Sans", Arial, sans-serif; font-weight: 400; fill: var(--ink); font-size: 17px; letter-spacing: .5px; }
  .write-line { stroke: var(--rule); stroke-width: 1.2; }
  .divider { stroke: var(--rule); stroke-width: 1.2; }
  .icon-disc { fill: var(--sun-yellow); }
  .icon-mark { fill: none; stroke: var(--paper); stroke-width: 1.6; stroke-linecap: round; }
  .icon-fill { fill: var(--paper); }
</style>
</head>
<body>
<main class="sheet">

  <!-- Front of card -->
  <section class="card card-front" aria-label="Card front">
    <svg viewBox="0 0 540 309" xmlns="http://www.w3.org/2000/svg">
      <defs>
        <radialGradient id="frontDark" cx="55%" cy="35%" r="70%">
          <stop offset="0" stop-color="#4a4a4a"/>
          <stop offset="1" stop-color="#262626"/>
        </radialGradient>
      </defs>
      <rect width="540" height="309" fill="url(#frontDark)"/>
      <path d="M0,100 C150,190 350,255 540,270 L540,309 L0,309 Z" fill="var(--sun-yellow)"/>
      <path d="M0,112 C150,200 350,265 540,280 L540,309 L0,309 Z" fill="var(--paper)"/>
      <circle class="brand-dot" cx="188" cy="92" r="16"/>
      <text class="brand-name" x="214" y="104" font-size="34">Brightfield Solar</text>
      <text class="web-address" x="96" y="218" transform="rotate(18 96 218)">www.brightfieldsolar.com</text>
    </svg>
  </section>

  <!-- Back of card: appointment -->
  <section class="card card-back" aria-label="Card back">
    <svg viewBox="0 0 540 309" xmlns="http://www.w3.org/2000/svg">
      <rect width="540" height="309" fill="var(--paper)"/>
      <path d="M0,105 C35,215 120,290 245,309 L0,309 Z" fill="var(--sun-yellow)"/>
      <path d="M0,122 C30,222 110,292 225,309 L0,309 Z" fill="var(--charcoal)"/>
      <path d="M370,0 C455,50 520,140 540,205 L540,0 Z" fill="var(--sun-yellow)"/>
      <path d="M388,0 C466,50 525,132 540,180 L540,0 Z" fill="var(--charcoal)"/>

      <circle class="brand-dot" cx="38" cy="120" r="9"/>
      <text class="brand-name" x="52" y="127" font-size="19">Brightfield Solar</text>

      <line class="divider" x1="228" y1="40" x2="228" y2="250"/>
      <text class="appointment-title" x="250" y="62">APPOINTMENT</text>

      <!-- date -->
      <circle class="icon-disc" cx="258" cy="98" r="10"/>
      <rect class="icon-mark" x="252.5" y="93" width="11" height="10" rx="1"/>
      <line class="icon-mark" x1="252.5" y1="96.5" x2="263.5" y2="96.5"/>
      <line class="write-line" x1="276" y1="106" x2="460" y2="106"/>
      <!-- time -->
      <circle class="icon-disc" cx="258" cy="140" r="10"/>
      <circle class="icon-mark" cx="258" cy="140" r="5.5"/>
      <path class="icon-mark" d="M258,137 V140 H261"/>
      <line class="write-line" x1="276" y1="148" x2="490" y2="148"/>
      <!-- employee -->
      <circle class="icon-disc" cx="258" cy="182" r="10"/>
      <circle class="icon-fill" cx="258" cy="179" r="3"/>
      <path class="icon-fill" d="M252.5,188 C253,183.5 263,183.5 263.5,188 Z"/>
      <line class="write-line" x1="276" y1="190" x2="500" y2="190"/>
      <!-- phone -->
      <circle class="icon-disc" cx="258" cy="224" r="10"/>
      <path class="icon-mark" d="M254,220 C254,226 257,229 262,229 L262,226.5 L259.5,225.5 L258.5,226.5 C257,225.5 256.5,225 255.8,223.5 L256.8,222.5 L256,220 Z"/>
      <line class="write-line" x1="276" y1="232" x2="500" y2="232"/>
    </svg>
  </section>

</main>
</body>
</html>
```